Business card design needed

I would like to use the print I have supplied with my Logo & info i have supplied.
On the back i would like a
*We Use & Recommend*
*Tarvin Filters
*Dulmok Oils
*QRV Spark Plugs
*Z-Blade Exhaust
*Colvane Brake Pads

*Your Next Appointment:

Industry/Entity Type

Business

Contact Information for Business Card

FERRIMS AUTO CENTRE
All Mechanical Repairs
Log Book Servicing
Authorised NSW Inspection station
Email: ferrimsautocentre@mailbox-example.com.au
17 Tumbrel Rd
P.O.Box 8270
Queanbeyan NSW 2629
0262480315

```html
<!DOCTYPE html>
<html lang="en">
<head>
<meta charset="utf-8">
<title>Ferrims Auto Centre – Business Card</title>
<link rel="stylesheet" href="https://fonts.googleapis.com/css2?family=Marcellus&family=Arimo:wght@400&display=swap">
<style>
  :root {
    --backdrop: #3a3a3a;
    --card-white: #ffffff;
    --card-grey: #e9e9e9;
    --brand-red: #b3201c;
    --brand-red-dark: #7e0f0c;
    --brand-red-light: #d8443a;
    --text-dark: #222222;
    --rule-grey: #9a9a9a;
  }
  * { box-sizing: border-box; margin: 0; padding: 0; }
  html, body {
    width: 1038px;
    height: 1200px;
    overflow: hidden;
    background: var(--backdrop);
  }
  .canvas { position: relative; width: 1038px; height: 1200px; }
  .card {
    position: absolute;
    left: 39px;
    width: 910px;
    overflow: hidden;
    background: radial-gradient(ellipse at 80% 30%, var(--card-white) 0%, var(--card-white) 35%, var(--card-grey) 100%);
    box-shadow: 0 6px 18px rgba(0,0,0,0.45);
  }
  .card--front { top: 41px; height: 517px; }
  .card--back  { top: 606px; height: 532px; }

  .card__band { position: absolute; left: 0; top: 0; width: 100%; height: 100%; }

  /* Front */
  .car-artwork {
    position: absolute;
    left: 0;
    top: 0;
    width: 740px;
    height: 420px;
    background:
      radial-gradient(ellipse at 40% 60%, #d9432a 0%, #b8281a 30%, rgba(184,40,26,0.35) 55%, rgba(255,255,255,0) 75%),
      linear-gradient(120deg, #c9c9c9 0%, #f2f2f2 60%, rgba(255,255,255,0) 100%);
    border-radius: 0 0 60% 0 / 0 0 30% 0;
  }
  .brand-name {
    font-family: "Marcellus", serif;
    color: var(--brand-red);
    font-weight: 400;
    letter-spacing: 0.5px;
    white-space: nowrap;
  }
  .tagline {
    font-family: "Arimo", sans-serif;
    color: var(--brand-red);
    font-size: 13.5px;
    white-space: nowrap;
  }
  .front-brand .brand-name {
    position: absolute; right: 24px; top: 428px;
    font-size: 38px; line-height: 40px;
  }
  .front-brand .tagline {
    position: absolute; right: 24px; top: 472px; line-height: 16px;
  }

  /* Back */
  .recommend-heading {
    position: absolute;
    left: 20px;
    top: 118px;
    width: 302px;
    text-align: right;
    font-family: "Arimo", sans-serif;
    font-size: 20px;
    color: var(--text-dark);
    white-space: nowrap;
  }
  .product-list {
    position: absolute;
    left: 20px;
    top: 160px;
    width: 302px;
    list-style: none;
    text-align: right;
    font-family: "Arimo", sans-serif;
    font-size: 30px;
    line-height: 36px;
    color: var(--brand-red);
    white-space: nowrap;
  }
  .divider {
    position: absolute;
    left: 354px;
    top: 103px;
    width: 1px;
    height: 280px;
    background: var(--rule-grey);
  }
  .back-brand { position: absolute; left: 380px; top: 108px; }
  .back-brand .brand-name { font-size: 40px; line-height: 44px; padding-left: 56px; }
  .back-brand .tagline { margin-top: 10px; }
  .contact-list {
    position: absolute;
    left: 384px;
    top: 208px;
    list-style: none;
    font-family: "Arimo", sans-serif;
    font-size: 22px;
    color: var(--text-dark);
  }
  .contact-item {
    display: flex;
    align-items: center;
    gap: 20px;
    height: 32px;
    margin-bottom: 30px;
    white-space: nowrap;
  }
  .contact-icon { width: 22px; height: 22px; flex: none; fill: var(--text-dark); }
  .appointment {
    position: absolute;
    left: 20px;
    top: 398px;
    width: 870px;
    display: flex;
    align-items: flex-end;
    gap: 14px;
    font-family: "Arimo", sans-serif;
    font-size: 20px;
    color: var(--brand-red);
    white-space: nowrap;
  }
  .appointment__line {
    flex: 1;
    height: 1px;
    margin-bottom: 5px;
    background: var(--rule-grey);
  }
</style>
</head>
<body>
<main class="canvas">

  <section class="card card--front" aria-label="Business card front">
    <div class="car-artwork" role="img" aria-label="Illustration of a red classic sedan with chrome wheels, shown twice"></div>
    <svg class="card__band" viewBox="0 0 910 517" preserveAspectRatio="none" aria-hidden="true">
      <path d="M0 455 C 250 525, 600 522, 910 500 L910 517 L0 517 Z" fill="var(--brand-red)"/>
      <path d="M0 478 C 280 535, 620 528, 910 510 L910 517 L0 517 Z" fill="var(--brand-red-dark)"/>
      <path d="M0 449 C 250 519, 600 516, 910 494" fill="none" stroke="var(--brand-red-light)" stroke-width="2"/>
    </svg>
    <div class="front-brand">
      <h1 class="brand-name">FERRIMS AUTO CENTRE</h1>
      <p class="tagline">All Mechanical Repairs Log Book Servicing Authorised NSW Inspection station</p>
    </div>
  </section>

  <section class="card card--back" aria-label="Business card back">
    <svg class="card__band" viewBox="0 0 910 532" preserveAspectRatio="none" aria-hidden="true">
      <path d="M0 470 C 300 520, 650 520, 910 455 L910 532 L0 532 Z" fill="var(--brand-red)"/>
      <path d="M0 495 C 300 540, 650 530, 910 480 L910 532 L0 532 Z" fill="var(--brand-red-dark)"/>
      <path d="M0 463 C 300 512, 650 512, 910 448" fill="none" stroke="var(--brand-red-light)" stroke-width="2"/>
    </svg>

    <p class="recommend-heading">We Use &amp; Recommend</p>
    <ul class="product-list">
      <li>Dulmok Oils</li>
      <li>Tarvin Filters</li>
      <li>Z-Blade Exhaust</li>
      <li>QRV Spark Plugs</li>
      <li>Colvane Brake Pads</li>
    </ul>

    <div class="divider"></div>

    <div class="back-brand">
      <h2 class="brand-name">FERRIMS AUTO CENTRE</h2>
      <p class="tagline">All Mechanical Repairs Log Book Servicing Authorised NSW Inspection station</p>
    </div>

    <ul class="contact-list">
      <li class="contact-item">
        <svg class="contact-icon" viewBox="0 0 24 24" aria-hidden="true">
          <rect x="1" y="1" width="22" height="22" rx="4"/>
          <path d="M8 6 l2 0 l1 4 l-2 1 a8 8 0 0 0 4 4 l1-2 l4 1 l0 2 a3 3 0 0 1-3 2 a11 11 0 0 1-10-10 a3 3 0 0 1 3-2z" fill="#fff"/>
        </svg>
        <span>0262480315</span>
      </li>
      <li class="contact-item">
        <svg class="contact-icon" viewBox="0 0 24 24" aria-hidden="true">
          <path d="M2 9 L12 2 L22 9 V21 H2 Z"/>
          <path d="M4 10 L12 15.5 L20 10" fill="none" stroke="#fff" stroke-width="1.8"/>
        </svg>
        <span>ferrimsautocentre@mailbox-example.com.au</span>
      </li>
      <li class="contact-item">
        <svg class="contact-icon" viewBox="0 0 24 24" aria-hidden="true">
          <path d="M12 1 a8 8 0 0 1 8 8 c0 6-8 14-8 14 s-8-8-8-14 a8 8 0 0 1 8-8z"/>
          <circle cx="12" cy="9" r="3" fill="#fff"/>
        </svg>
        <span>17 Tumbrel Rd P.O.Box 8270 Queanbeyan</span>
      </li>
    </ul>

    <div class="appointment">
      <span>Your Next Appointment:</span>
      <span class="appointment__line"></span>
    </div>
  </section>

</main>
</body>
</html>
```